Updated brief for New ecommerce site needs a stunning business card that links to web site.

Updated business card brief. Please refer to the new files uploaded today (the last two) which show the background colour/style that we will be using in our web template for on-line trading, the grey marble concrete look.

Please see if you can use the grey marble background in the business card design in a way so it relates to our web template. It also needs to be transferable to banner ad, chatterbay ad etc.
brivo hub is a NEW eCommerce website which is commencing selling via tradlo & sellnook, used & damaged mobile phones & accessories, evolving into a full eCommerce store.

We like strong clean lines, use of a circle, in essence this will become our logo as well. Colours strong orange/Black/White The orange stronger than in CraftPanel #5352704 & grey marble as per file attached #153082

We love the use of a circle!! As we are evolving & moving forward this is what the circle represents to us……. ongoing change.

Front side with a circle with brivo hub in a modern font in the middle, brivo is in a strong orange and group is in black or white. On the reverse side, use layout as per Lumerax design from pelk.example. for icon details (not the boarder at top/botto).

This design is to meet www.pelk.example luxe cards specifications
Thank you we look forward to last minute inspiration.
Updates

Target Market(s)

Suppliers & business networking

Industry/Entity Type

Business

Contact Information for Business Card

Sam Ruiz
Director
mob +61 4987 6543
Locked Bag WXYZ 5678 QRS
sam@brivohub.example.au
www.brivohub.example.au

Requirements
Must have
• Design to meet www.pelk.example luxe business card specifications
• Colours - orange needs to be bold and strong & /black/white
• Circle with brivo hub in the middle
Nice to have
• Grey marble background incorporated into design in someway so it links with our web page.

```html
<!DOCTYPE html>
<html lang="en">
<head>
<meta charset="utf-8">
<title>brivohub business card</title>
<link rel="stylesheet" href="https://fonts.googleapis.com/css2?family=Iceland&display=swap">
<style>
  :root {
    --stage: #1c1c1c;
    --orange: #d4561d;
    --orange-deep: #b8461a;
    --orange-soft: #e98a5a;
    --charcoal: #2b2b2b;
    --ink: #262626;
    --paper: #ffffff;
    --circle: #ececec;
    --text-light: #f2f2f2;
  }
  * { box-sizing: border-box; margin: 0; padding: 0; }
  html, body {
    width: 1200px;
    height: 871px;
    overflow: hidden;
  }
  body {
    background: var(--stage);
    font-family: "Iceland", "Arial Narrow", sans-serif;
    font-weight: 400;
    display: flex;
    align-items: center;
    justify-content: center;
    gap: 120px;
  }
  .card {
    width: 340px;
    height: 540px;
    border-radius: 4px;
    position: relative;
    overflow: hidden;
  }

  /* Front */
  .card-front {
    background: linear-gradient(160deg, var(--orange) 0%, var(--orange-deep) 100%);
    display: flex;
    align-items: center;
    justify-content: center;
  }
  .logo-circle {
    width: 250px;
    height: 250px;
    border-radius: 50%;
    background: var(--circle);
    display: flex;
    align-items: center;
    justify-content: center;
  }
  .wordmark {
    font-size: 54px;
    font-weight: 400;
    letter-spacing: 1px;
    color: var(--orange);
    white-space: nowrap;
  }

  /* Back */
  .card-back {
    background: var(--paper);
    padding: 18px 18px 0;
    display: flex;
    flex-direction: column;
  }
  .contact-panel {
    background: var(--charcoal);
    height: 390px;
    padding: 40px 22px 0 26px;
    color: var(--text-light);
    overflow: hidden;
  }
  .name {
    font-size: 50px;
    font-weight: 400;
    color: var(--orange-soft);
    line-height: 1;
    white-space: nowrap;
  }
  .role {
    font-size: 28px;
    font-weight: 400;
    letter-spacing: 3px;
    margin-top: 4px;
  }
  .contact-list {
    list-style: none;
    margin-top: 40px;
  }
  .contact-list li {
    display: flex;
    align-items: center;
    gap: 12px;
    font-size: 16px;
    font-weight: 400;
    letter-spacing: 0.8px;
    margin-bottom: 22px;
    white-space: nowrap;
  }
  .contact-list svg {
    width: 16px;
    height: 16px;
    flex: none;
  }
  .brand-strip {
    flex: 1;
    display: flex;
    align-items: center;
    justify-content: center;
  }
  .brand-strip .wordmark {
    font-size: 48px;
    color: var(--ink);
  }
</style>
</head>
<body>

  <section class="card card-front" aria-label="Card front">
    <div class="logo-circle">
      <span class="wordmark">brivohub</span>
    </div>
  </section>

  <section class="card card-back" aria-label="Card back">
    <div class="contact-panel">
      <h1 class="name">Sam Ruiz</h1>
      <p class="role">Director</p>
      <ul class="contact-list">
        <li>
          <svg viewBox="0 0 18 18" aria-hidden="true"><rect x="5" y="1" width="8" height="16" rx="1.5" fill="none" stroke="var(--orange-soft)" stroke-width="1.6"/><line x1="8" y1="14.5" x2="10" y2="14.5" stroke="var(--orange-soft)" stroke-width="1.6"/></svg>
          <span>+61 4987 6543</span>
        </li>
        <li>
          <svg viewBox="0 0 18 18" aria-hidden="true"><rect x="1.5" y="4" width="15" height="10" fill="none" stroke="var(--orange-soft)" stroke-width="1.6"/><polyline points="1.5,4 9,10 16.5,4" fill="none" stroke="var(--orange-soft)" stroke-width="1.6"/></svg>
          <span>sam@brivohub.example.au</span>
        </li>
        <li>
          <svg viewBox="0 0 18 18" aria-hidden="true"><circle cx="9" cy="9" r="7.5" fill="none" stroke="var(--orange-soft)" stroke-width="1.6"/><ellipse cx="9" cy="9" rx="3.2" ry="7.5" fill="none" stroke="var(--orange-soft)" stroke-width="1.2"/><line x1="1.5" y1="9" x2="16.5" y2="9" stroke="var(--orange-soft)" stroke-width="1.2"/></svg>
          <span>www.brivohub.example.au</span>
        </li>
        <li>
          <svg viewBox="0 0 18 18" aria-hidden="true"><path d="M9 17 C5 11.5 3.5 9 3.5 6.5 A5.5 5.5 0 0 1 14.5 6.5 C14.5 9 13 11.5 9 17 Z" fill="var(--orange-soft)"/><circle cx="9" cy="6.5" r="2" fill="var(--charcoal)"/></svg>
          <span>Locked Bag WXYZ 5678 QRS</span>
        </li>
      </ul>
    </div>
    <div class="brand-strip">
      <span class="wordmark">brivohub</span>
    </div>
  </section>

</body>
</html>
```